Software as a Service to manage Home Care Management

We need a web site designed for Home Care Management Software as a Service product, that facilitates Home Care organizations to manage and schedule carers to visit client homes. We want a modern look and feel using our existing logo.

Target Market(s)

Home Care Management organizations. Product is similar to: https://kelvantro.co/

Coding

Coded - Design and coding required

Number of Pages Required

3 page

```html
<!DOCTYPE html>
<html lang="en">
<head>
<meta charset="utf-8">
<title>Hearthline – Home Care Management</title>
<link href="https://fonts.googleapis.com/css2?family=Lato:wght@300;400;700&display=swap" rel="stylesheet">
<style>
:root{
  --pink:#f5427a;
  --ink:#333333;
  --grey-text:#4a4a4a;
  --blue:#2a86c9;
  --dark-band:#5b5b5b;
  --bottom-bar:#555555;
  --white:#ffffff;
  --hero-light:#f1f1f1;
}
*{box-sizing:border-box;margin:0;padding:0}
html,body{width:1200px;height:4500px;overflow:hidden}
body{position:relative;background:var(--white);font-family:'Lato',sans-serif;color:var(--ink)}
.abs{position:absolute}
.top-rule{left:0;top:0;width:1200px;height:3px;background:#222}
.brand{display:flex;align-items:center;gap:12px}
.brand-mark{width:52px;height:52px;border-radius:50%;background:var(--pink)}
.brand-name{font-size:30px;font-weight:400;color:var(--ink);letter-spacing:1px}
.site-header .brand{left:136px;top:66px}
.main-nav a{position:absolute;top:103px;font-size:13px;font-weight:700;color:#777;text-decoration:none;letter-spacing:.5px}
.main-nav a.active{color:var(--pink)}
.hero{left:0;top:175px;width:1200px;height:576px;background:linear-gradient(90deg,#c9b8a8 0%,#d8cfc7 35%,#ebe8e6 52%,var(--hero-light) 62%,var(--hero-light) 100%)}
.hero-title{left:652px;top:268px;font-size:37px;font-weight:400;line-height:43px;color:var(--ink)}
.hero-text{left:652px;top:356px;width:500px;font-size:24px;font-weight:300;line-height:31px;color:var(--grey-text)}
.btn{display:flex;align-items:center;justify-content:center;background:var(--pink);color:var(--white);font-size:17px;font-weight:300;text-decoration:none}
.hero-btn{left:660px;top:514px;width:266px;height:70px;font-weight:700;font-size:16px}
.slider-dots{left:672px;top:712px;display:flex;gap:6px}
.slider-dots span{width:16px;height:16px;border-radius:50%;border:2px solid var(--white)}
.slider-dots span.on{background:var(--white)}
.phone{left:259px;top:856px;width:176px;height:370px;border-radius:22px;background:#1e1e1e;padding:54px 10px 54px}
.phone-screen{width:100%;height:100%;background:linear-gradient(180deg,#2aa7d9 0 24px,#f4f7f9 24px)}
.feature-title{left:535px;top:846px;font-size:35px;line-height:43px;font-weight:400;color:var(--ink)}
.feature-list{left:535px;top:950px;list-style:none}
.feature-list li{display:flex;align-items:center;gap:22px;height:43.4px;font-size:16px;font-weight:300;color:var(--ink)}
.feature-list svg{width:17px;height:17px;flex:none}
.btn-readmore-feature{left:535px;top:1272px;width:150px;height:47px}
.btn-demo{left:718px;top:1272px;width:152px;height:47px;background:#1c1c1c}
.section-title{left:0;width:1200px;text-align:center;font-size:46px;font-weight:300;color:#444;letter-spacing:1px}
.audience{width:320px;text-align:center;top:1559px}
.audience .ring{margin:0 auto;width:156px;height:156px;border-radius:50%;border:2px solid var(--pink);display:flex;align-items:center;justify-content:center}
.audience .ring.dark{border-color:#222}
.audience h3{margin-top:47px;font-size:22px;font-weight:700;color:var(--ink)}
.audience p{margin-top:20px;font-size:18px;font-weight:300;line-height:24px;color:var(--ink)}
.photo{background:linear-gradient(135deg,#6a7f8f,#2fa8d8 60%,#b9c4cb)}
.stat{display:flex;flex-direction:column;align-items:center}
.stat-num{font-size:36px;font-weight:700;color:var(--blue)}
.stat-label{font-size:14px;color:var(--blue);text-align:center;line-height:19px}
.stat .btn{width:152px;height:48px}
.partner{background:#5a5a5a}
.contact{left:0;top:3171px;width:1200px;height:716px;background:var(--dark-band)}
.field-label{font-size:16px;font-weight:300;color:var(--white)}
.field{background:var(--white);border:1px solid #ddd}
.contact-title{left:638px;top:3284px;font-size:33px;font-weight:300;color:var(--white)}
.contact-text{left:638px;top:3357px;font-size:16px;font-weight:300;line-height:36px;color:var(--white)}
.site-footer{left:0;top:3887px;width:1200px;height:481px;background:var(--pink)}
.footer-head{font-size:13px;font-weight:700;color:var(--white)}
.footer-link{font-size:13px;font-weight:300;color:var(--white)}
.social{width:60px;height:59px;background:var(--white);border-radius:6px;display:flex;align-items:center;justify-content:center}
.social span{width:28px;height:28px;background:var(--pink);border-radius:4px}
.bottom-bar{left:0;top:4368px;width:1200px;height:78px;background:var(--bottom-bar);color:var(--white);font-size:16px;font-weight:300;display:flex;align-items:center;justify-content:center}
</style>
</head>
<body>
<div class="abs top-rule"></div>

<header class="site-header">
  <div class="abs brand"><span class="brand-mark"></span><span class="brand-name">Hearthline</span></div>
  <nav class="main-nav">
    <a class="active" style="left:536px">PRODUCT</a>
    <a style="left:646px">PRICING</a>
    <a style="left:739px">BLOG</a>
    <a style="left:819px">FAQ</a>
    <a style="left:887px">CONTACT US</a>
    <a style="left:1020px">LOG IN</a>
  </nav>
</header>

<section>
  <div class="abs hero" role="img" aria-label="Photo of a smiling carer with an older woman holding a walking cane"></div>
  <h1 class="abs hero-title">MORE THAN A CARE<br>SOFTWARE PROVIDER</h1>
  <p class="abs hero-text">At Warm Hands, we are passionate about we do and believe everyone has the right to age with dignity in the comfort and place of their choosing.</p>
  <a class="abs btn hero-btn">SEE HOW IT WORKS</a>
  <div class="abs slider-dots"><span></span><span class="on"></span><span></span><span></span></div>
</section>

<section>
  <div class="abs phone" role="img" aria-label="Smartphone showing the carer visit schedule app"><div class="phone-screen"></div></div>
  <h2 class="abs feature-title">OPTIMISED HOME<br>CARE SOFTWARE</h2>
  <ul class="abs feature-list">
    <li><svg viewBox="0 0 20 20"><circle cx="10" cy="10" r="8.5" fill="none" stroke="#f5427a" stroke-width="2"/><path d="M6 10l3 3 5-6" fill="none" stroke="#f5427a" stroke-width="2"/></svg>Optimised Home Care Software</li>
    <li><svg viewBox="0 0 20 20"><circle cx="10" cy="10" r="8.5" fill="none" stroke="#f5427a" stroke-width="2"/><path d="M6 10l3 3 5-6" fill="none" stroke="#f5427a" stroke-width="2"/></svg>All-in-one home care software</li>
    <li><svg viewBox="0 0 20 20"><circle cx="10" cy="10" r="8.5" fill="none" stroke="#f5427a" stroke-width="2"/><path d="M6 10l3 3 5-6" fill="none" stroke="#f5427a" stroke-width="2"/></svg>Create staff rotas with automated scheduling tools</li>
    <li><svg viewBox="0 0 20 20"><circle cx="10" cy="10" r="8.5" fill="none" stroke="#f5427a" stroke-width="2"/><path d="M6 10l3 3 5-6" fill="none" stroke="#f5427a" stroke-width="2"/></svg>Tailored care plans &amp; risk assessments for your clients</li>
    <li><svg viewBox="0 0 20 20"><circle cx="10" cy="10" r="8.5" fill="none" stroke="#f5427a" stroke-width="2"/><path d="M6 10l3 3 5-6" fill="none" stroke="#f5427a" stroke-width="2"/></svg>Check in/out from a client visit using the app</li>
    <li><svg viewBox="0 0 20 20"><circle cx="10" cy="10" r="8.5" fill="none" stroke="#f5427a" stroke-width="2"/><path d="M6 10l3 3 5-6" fill="none" stroke="#f5427a" stroke-width="2"/></svg>Reporting suite for payroll, invoices, inspections &amp; more!</li>
    <li><svg viewBox="0 0 20 20"><circle cx="10" cy="10" r="8.5" fill="none" stroke="#f5427a" stroke-width="2"/><path d="M6 10l3 3 5-6" fill="none" stroke="#f5427a" stroke-width="2"/></svg>Easy to set up and use. Get started today!</li>
  </ul>
  <a class="abs btn btn-readmore-feature">Readmore</a>
  <a class="abs btn btn-demo">Book Free Demo</a>
</section>

<section>
  <h2 class="abs section-title" style="top:1418px">WE HAVE MADE KELVANTRO...</h2>
  <div class="abs audience" style="left:125px">
    <div class="ring"><svg width="74" height="50" viewBox="0 0 74 50"><path d="M6 42L2 10l18 16L37 4l17 22 18-16-4 32z" fill="none" stroke="#333" stroke-width="2.5" stroke-linejoin="round"/><line x1="8" y1="46" x2="66" y2="46" stroke="#333" stroke-width="2.5"/></svg></div>
    <h3>FOR MANAGERS</h3>
    <p>Care management tools<br>that save your time and money.<br>Enables you to grow your business.</p>
  </div>
  <div class="abs audience" style="left:438px">
    <div class="ring dark"><svg width="56" height="50" viewBox="0 0 56 50"><path d="M28 46S4 31 4 16A12 12 0 0 1 28 10a12 12 0 0 1 24 6c0 15-24 30-24 30z" fill="none" stroke="#f5427a" stroke-width="3.5" stroke-linejoin="round"/></svg></div>
    <h3>FOR CARERS</h3>
    <p>Simple and easy to use App.<br>Rosters and care plans on the go.<br>More time for care.</p>
  </div>
  <div class="abs audience" style="left:761px">
    <div class="ring"><svg width="52" height="44" viewBox="0 0 52 44"><path d="M26 2L2 22h7v20h12V30h10v12h12V22h7z" fill="#333"/></svg></div>
    <h3>FOR CLIENTS AND FAMILIES</h3>
    <p>Latest information in real time,<br>all documents in one place.<br>Transparency for all.</p>
  </div>
</section>

<section>
  <h2 class="abs section-title" style="top:2016px">SUCCESS IN NUMBERS</h2>
  <div class="abs photo" style="left:31px;top:2124px;width:379px;height:252px" role="img" aria-label="Photo of a carer in a blue uniform helping a client at home"></div>
  <div class="abs stat" style="left:410px;top:2124px;width:381px;height:252px;padding-top:42px">
    <div class="stat-num">96%</div>
    <div class="stat-label" style="margin-top:16px">Customer support happiness</div>
    <a class="btn" style="margin-top:24px">Readmore</a>
  </div>
  <div class="abs photo" style="left:791px;top:2124px;width:380px;height:252px" role="img" aria-label="Photo of a smiling carer beside an older man in a wheelchair"></div>
  <div class="abs stat" style="left:31px;top:2376px;width:379px;height:255px;padding-top:16px">
    <div class="stat-num">13M</div>
    <div class="stat-label" style="margin-top:12px">Total care hours<br>managed by Kelvantro</div>
    <a class="btn" style="margin-top:52px">Readmore</a>
  </div>
  <div class="abs photo" style="left:410px;top:2376px;width:381px;height:255px" role="img" aria-label="Photo of a carer walking outdoors with an older man"></div>
  <div class="abs stat" style="left:791px;top:2376px;width:380px;height:255px;padding-top:24px">
    <div class="stat-num">17K</div>
    <div class="stat-label" style="margin-top:12px">Active Kelvantro users</div>
    <a class="btn" style="margin-top:66px">Readmore</a>
  </div>
</section>

<section>
  <h2 class="abs section-title" style="top:2842px">WORKING ASSOCIATE WITH</h2>
  <div class="abs partner" style="left:124px;top:2944px;width:112px;height:128px;border-radius:4px"></div>
  <div class="abs partner" style="left:332px;top:2980px;width:268px;height:80px;border-radius:40px"></div>
  <div class="abs partner" style="left:630px;top:2972px;width:234px;height:86px;border-radius:43px"></div>
  <div class="abs partner" style="left:980px;top:2966px;width:112px;height:96px;border-radius:4px"></div>
</section>

<section class="abs contact">
  <div class="abs field-label" style="left:180px;top:91px">Name</div>
  <div class="abs field" style="left:178px;top:122px;width:386px;height:35px"></div>
  <div class="abs field-label" style="left:180px;top:183px">Company name</div>
  <div class="abs field" style="left:178px;top:215px;width:386px;height:35px"></div>
  <div class="abs field-label" style="left:180px;top:278px">Phone Number</div>
  <div class="abs field" style="left:178px;top:302px;width:386px;height:35px"></div>
  <div class="abs field-label" style="left:180px;top:370px">Email</div>
  <div class="abs field" style="left:178px;top:391px;width:386px;height:35px"></div>
  <div class="abs field-label" style="left:180px;top:463px">Demo Date</div>
  <div class="abs field-label" style="left:399px;top:463px">Time</div>
  <div class="abs field" style="left:178px;top:484px;width:166px;height:35px"></div>
  <div class="abs field" style="left:397px;top:484px;width:166px;height:35px"></div>
  <a class="abs btn" style="left:180px;top:568px;width:150px;height:47px">Book Now</a>
</section>
<h2 class="abs contact-title">Want to know More ?</h2>
<p class="abs contact-text">Get a full overview of the Hearthline<br>Care Management platform.<br>Book an Online Demo with our product team!<br>Schedule a live online demo of our key features,<br>and see how you can save time and money.</p>

<footer class="abs site-footer">
  <div class="abs brand" style="left:166px;top:66px"><span class="brand-mark" style="background:#fff"></span><span class="brand-name" style="color:#fff">Hearthline</span></div>
  <div class="abs footer-head" style="left:196px;top:164px">APP</div>
  <div class="abs footer-link" style="left:196px;top:201px">Managers</div>
  <div class="abs footer-link" style="left:196px;top:238px">Carers</div>
  <div class="abs footer-link" style="left:196px;top:273px">Customers &amp; Family</div>
  <div class="abs footer-head" style="left:356px;top:164px">ABOUT US</div>
  <div class="abs footer-link" style="left:356px;top:201px">Contact us</div>
  <div class="abs footer-link" style="left:356px;top:238px">Work with us</div>
  <div class="abs" style="left:612px;top:50px;font-size:30px;font-weight:300;color:#fff">Get the latest news from us!</div>
  <div class="abs footer-link" style="left:615px;top:113px;font-size:16px;line-height:30px">Join our newsletter to stay up to date<br>on features and releases</div>
  <div class="abs" style="left:617px;top:189px;width:384px;height:42px;background:#fff;border-radius:4px;padding:12px 18px;font-size:13px;font-weight:700;color:#333">Email</div>
  <a class="abs btn" style="left:617px;top:260px;width:150px;height:47px;background:#555;font-size:13px;font-weight:700">Subscribe</a>
  <div class="abs social" style="left:482px;top:362px"><span></span></div>
  <div class="abs social" style="left:571px;top:362px"><span></span></div>
  <div class="abs social" style="left:662px;top:362px"><span></span></div>
</footer>
<div class="abs bottom-bar">© 2020 Hearthline. All rights reserved. Terms &amp; Privacy</div>
</body>
</html>
```